Modify mobile web Photoshop design to make them look great

We need to choose and refine the stock image to look great on 5 mobile web pages: 1) Hourglass image on home screen, 2) Sofa image on registration screen, 3) Loveseat image on login screen, 4) Lamp for reminder screen, and 5) Bed for ratings / score screen. Sample photos denote what customer wants, but they are just downloaded from Vantry, and is not purchased stock photos. Designers need to show that the updated photos used are properly purchased from stock photo source. Photoshop files for all 5 mobile web pages are provided. Artists are requested to edit and submit the 5 photoshop files and make them look as good as possible with the constraints above. No change is needed on the layout or anything beside the 5 stock images, but subtle refinements are OK if you believe it would improve the overall design without affecting the art direction.

Target Market(s)

Travel, Lifestyle

Industry/Entity Type

Hospitality

Font styles to use
Sans Serif

Requirements
Must have
• Stock photos must be properly licensed, artists must put updated stock photos back into supplied photoshop source files, updated look and feel should have the same general art direction, images must be hourglass, sofa, loveseat, lamp and bed
Nice to have
• Minor and very subtle touchup of other elements without affecting any design work of the layout such as color scheme
Should not have
• Should not affect art direction, identity and color of all design and layout elements, should not use stock image other than the types specified (hourglass, sofa, loveseat, lamp and bed), should not use images not licensed from stock photo sites

```html
<!DOCTYPE html>
<html lang="en">
<head>
<meta charset="utf-8">
<title>Restly – Booking Reminder</title>
<link rel="stylesheet" href="https://fonts.googleapis.com/css2?family=Source+Sans+3:wght@400;600;700&display=swap">
<style>
  :root {
    --ink: #111111;
    --muted: #666666;
    --white: #ffffff;
    --bg-top: #f6f6f6;
    --bg-bottom: #e4e4e4;
    --card: rgba(255, 255, 255, 0.86);
    --chip: #d9d9d9;
    --teal: #0f9a98;
    --magenta: #a3137c;
    --lilac: #b07ad8;
    --peach: #f2b183;
    --cord-left: #8a5bc4;
    --cord-right: #17937e;
  }
  * { box-sizing: border-box; margin: 0; padding: 0; }
  html, body { width: 866px; height: 1200px; overflow: hidden; }
  body {
    font-family: "Source Sans 3", sans-serif;
    color: var(--ink);
    background: var(--white);
  }
  .screen {
    position: relative;
    width: 866px;
    height: 1200px;
    overflow: hidden;
    background: linear-gradient(180deg, var(--bg-top) 0%, var(--bg-bottom) 100%);
    border: 1px solid #333;
  }
  .app-bar {
    position: absolute;
    left: 0; top: 0;
    width: 100%; height: 104px;
    background: var(--white);
  }
  .back-button { position: absolute; left: 28px; top: 30px; }
  .menu-button { position: absolute; right: 24px; top: 36px; }
  .brand {
    position: absolute;
    left: 50%; top: 14px;
    transform: translateX(-50%);
    font-weight: 700;
    font-size: 62px;
    line-height: 1;
    color: var(--magenta);
    letter-spacing: -1px;
  }
  .lamp {
    position: absolute;
    top: 104px;
    height: 492px;
    width: 152px;
    border-radius: 0 0 76px 76px;
  }
  .lamp--left {
    left: 106px;
    background: linear-gradient(180deg, var(--cord-left) 0%, #d8d0de 30%, #ece8f0 60%, #e2dde8 100%);
  }
  .lamp--right {
    left: 612px;
    background: linear-gradient(180deg, var(--cord-right) 0%, #cfdcd8 30%, #e8efed 60%, #dde6e3 100%);
  }
  .reminder-card {
    position: absolute;
    left: 27px; top: 274px;
    width: 810px; height: 666px;
    background: var(--card);
    border-radius: 8px;
    text-align: center;
  }
  .alarm-icon { position: absolute; left: 346px; top: 69px; }
  .greeting {
    position: absolute;
    left: 0; right: 0; top: 282px;
    font-size: 36px;
    font-weight: 400;
  }
  .message {
    position: absolute;
    left: 40px; right: 40px; top: 358px;
    font-size: 28px;
    line-height: 42px;
  }
  .duration {
    position: absolute;
    top: 473px;
    width: 148px; height: 52px;
    background: var(--chip);
    border-radius: 12px;
    font-size: 33px;
    font-weight: 600;
    line-height: 52px;
  }
  .duration--one { left: 228px; }
  .duration--two { left: 439px; }
  .action {
    position: absolute;
    top: 542px;
    width: 184px; height: 49px;
    color: var(--white);
    font-size: 28px;
    line-height: 49px;
  }
  .action--cancel { left: 209px; background: var(--teal); }
  .action--continue { left: 420px; background: var(--magenta); }
  .charge-note {
    position: absolute;
    left: 0; right: 0; top: 600px;
    font-size: 23px;
    color: var(--muted);
  }
  .charge-note .mark { color: var(--magenta); }
  .pager {
    position: absolute;
    left: 330px; top: 1143px;
    display: flex;
    gap: 17px;
  }
  .pager-dot { width: 28px; height: 28px; border-radius: 50%; }
  .pager-dot--lilac { background: var(--lilac); }
  .pager-dot--teal { background: var(--teal); }
  .pager-dot--magenta { background: var(--magenta); }
  .pager-dot--peach { background: var(--peach); }
</style>
</head>
<body>
<main class="screen">
  <header class="app-bar">
    <svg class="back-button" width="32" height="46" viewBox="0 0 32 46" aria-label="Back">
      <polyline points="26,4 7,23 26,42" fill="none" stroke="#111" stroke-width="7"/>
    </svg>
    <div class="brand">restly.co</div>
    <svg class="menu-button" width="46" height="28" viewBox="0 0 46 28" aria-label="Menu">
      <g stroke="#111" stroke-width="3">
        <line x1="0" y1="2" x2="46" y2="2"/>
        <line x1="0" y1="14" x2="46" y2="14"/>
        <line x1="0" y1="26" x2="46" y2="26"/>
      </g>
    </svg>
  </header>

  <div class="lamp lamp--left" role="img" aria-label="Pendant light bulb hanging from a purple cord"></div>
  <div class="lamp lamp--right" role="img" aria-label="Pendant light bulb hanging from a green cord"></div>

  <section class="reminder-card">
    <svg class="alarm-icon" width="176" height="176" viewBox="0 0 176 176" aria-label="Alarm clock">
      <g fill="none" stroke="var(--magenta)" stroke-width="6" stroke-linecap="round">
        <path d="M10 40 A28 28 0 0 1 52 10 Z" stroke-linejoin="round"/>
        <path d="M166 40 A28 28 0 0 0 124 10 Z" stroke-linejoin="round"/>
        <circle cx="88" cy="94" r="68"/>
        <line x1="44" y1="150" x2="32" y2="168"/>
        <line x1="132" y1="150" x2="144" y2="168"/>
        <line x1="88" y1="88" x2="88" y2="42"/>
        <line x1="94" y1="94" x2="124" y2="94"/>
      </g>
      <circle cx="88" cy="94" r="8" fill="none" stroke="var(--magenta)" stroke-width="5"/>
      <g fill="var(--magenta)">
        <circle cx="88" cy="36" r="3"/><circle cx="88" cy="152" r="3"/>
        <circle cx="30" cy="94" r="3"/><circle cx="146" cy="94" r="3"/>
        <circle cx="117" cy="44" r="3"/><circle cx="138" cy="65" r="3"/>
        <circle cx="138" cy="123" r="3"/><circle cx="117" cy="144" r="3"/>
        <circle cx="59" cy="144" r="3"/><circle cx="38" cy="123" r="3"/>
        <circle cx="38" cy="65" r="3"/><circle cx="59" cy="44" r="3"/>
      </g>
    </svg>
    <h1 class="greeting">Hello John Doe,</h1>
    <p class="message">Your booked time remian 30 mins more. If you want to continue please click continue.</p>
    <div class="duration duration--one">1 hour</div>
    <div class="duration duration--two">2 hour</div>
    <div class="action action--cancel">Cancel</div>
    <div class="action action--continue">Continue</div>
    <p class="charge-note"><span class="mark">*</span> If you continue, charges will be applied hourly.</p>
  </section>

  <nav class="pager" aria-label="Screens">
    <span class="pager-dot pager-dot--lilac"></span>
    <span class="pager-dot pager-dot--teal"></span>
    <span class="pager-dot pager-dot--magenta"></span>
    <span class="pager-dot pager-dot--peach"></span>
    <span class="pager-dot pager-dot--teal"></span>
  </nav>
</main>
</body>
</html>
```